Presentation Folder, Business Card, Letterhead and Envelope design

We are a dental clinic that will open in August and we are looking for a professional graphic designer to create our Business Card, Presentation Folder, Letterhead, Notepad and envelopes.

The brand LumaGrin must reflect a sense of quality and sophistication, marketed for middle-class consumers.
Our preference is for quality and refined materials, where less is more.
Attached the logo

```html
<!DOCTYPE html>
<html lang="en">
<head>
<meta charset="utf-8">
<title>LumaGrin Business Card</title>
<link href="https://fonts.googleapis.com/css2?family=Montserrat:wght@300;700&family=Work+Sans:wght@400&display=swap" rel="stylesheet">
<style>
  :root {
    --maroon: #6b1413;
    --graphite: #5b5b5d;
    --ink: #3a3a3c;
    --paper: #ffffff;
    --backdrop: #2a2a2b;
  }
  * { margin: 0; padding: 0; box-sizing: border-box; }
  html, body { width: 1200px; height: 878px; overflow: hidden; }
  body {
    background: var(--backdrop);
    display: flex;
    align-items: center;
    justify-content: center;
    gap: 40px;
  }
  .card {
    width: 560px;
    height: 320px;
    position: relative;
    overflow: hidden;
    box-shadow: 0 10px 30px rgba(0,0,0,.45);
  }
  .card-back {
    background: var(--maroon);
    display: flex;
    align-items: center;
    justify-content: center;
  }
  .brand {
    display: flex;
    align-items: center;
    gap: 12px;
    font-family: "Montserrat", sans-serif;
    font-weight: 300;
    letter-spacing: .28em;
    text-transform: uppercase;
  }
  .brand-square { width: 22px; height: 22px; flex: none; }
  .card-back .brand { color: var(--paper); font-size: 34px; }
  .card-back .brand-square { background: var(--paper); width: 28px; height: 28px; }

  .card-front { background: var(--paper); }
  .card-front .brand {
    position: absolute;
    left: 34px;
    top: 136px;
    color: var(--graphite);
    font-size: 24px;
    gap: 10px;
  }
  .card-front .brand-square { background: var(--maroon); }
  .divider {
    position: absolute;
    left: 318px;
    top: 78px;
    width: 1.5px;
    height: 184px;
    background: var(--maroon);
  }
  .contact {
    position: absolute;
    left: 338px;
    top: 76px;
    font-family: "Work Sans", sans-serif;
    color: var(--ink);
  }
  .person-name {
    font-family: "Montserrat", sans-serif;
    font-weight: 700;
    font-size: 20px;
    letter-spacing: .04em;
    color: var(--maroon);
    text-transform: uppercase;
    line-height: 1.1;
  }
  .person-role { font-size: 13px; letter-spacing: .05em; margin-bottom: 14px; }
  .address { font-size: 13px; line-height: 1.35; letter-spacing: .04em; margin-bottom: 10px; }
  .contact-line {
    display: flex;
    align-items: center;
    gap: 8px;
    font-size: 14px;
    letter-spacing: .03em;
    line-height: 1.5;
  }
  .contact-line svg { width: 11px; height: 11px; flex: none; }
  .edge-bands { position: absolute; left: 0; bottom: 0; width: 560px; height: 16px; }
</style>
</head>
<body>
  <section class="card card-back" aria-label="Card back">
    <div class="brand"><span class="brand-square"></span><span>LumaGrin</span></div>
  </section>

  <section class="card card-front" aria-label="Card front">
    <div class="brand"><span class="brand-square"></span><span>LumaGrin</span></div>
    <div class="divider"></div>
    <div class="contact">
      <p class="person-name">Daniel Hart</p>
      <p class="person-role">Director</p>
      <p class="address">418 Willow Bend Road<br>Kansas City, MO 64108</p>
      <p class="contact-line">
        <svg viewBox="0 0 12 12"><path d="M3 1 L5 3.5 L4 5 Q5 7 7 8 L8.5 7 L11 9 L9.5 11 Q4 10.5 1 2.5 Z" fill="var(--maroon)"/></svg>
        +330 5172-4410
      </p>
      <p class="contact-line">
        <svg viewBox="0 0 12 12"><rect x="1" y="2.5" width="10" height="7" fill="none" stroke="var(--maroon)" stroke-width="1.2"/><path d="M1 2.5 L6 6.5 L11 2.5" fill="none" stroke="var(--maroon)" stroke-width="1.2"/></svg>
        info@lumagrin.com
      </p>
      <p class="contact-line">
        <svg viewBox="0 0 12 12"><circle cx="6" cy="6" r="5" fill="none" stroke="var(--maroon)" stroke-width="1"/><ellipse cx="6" cy="6" rx="2.2" ry="5" fill="none" stroke="var(--maroon)" stroke-width="1"/><path d="M1 6 H11" stroke="var(--maroon)" stroke-width="1"/></svg>
        www.lumagrin.com
      </p>
    </div>
    <svg class="edge-bands" viewBox="0 0 560 16" preserveAspectRatio="none">
      <polygon points="0,4 300,12 290,16 0,16" fill="var(--graphite)"/>
      <polygon points="312,8 560,14 560,16 300,16" fill="var(--maroon)"/>
    </svg>
  </section>
</body>
</html>
```